An international recruitment business looking to attract new engineering and construction clients i

BK Worldwide is an international recruitment company with a wealth of experienced engineers, quantity surveyors and construction specialists appropriate to fill roles in the vastly growing Middle East. We need a new, attractive brochure design to send to new clients/companies so they will be interested in our recruitment company and our candidates. We have provided our company logo which we would like to feature, and we would like the theme to match this to some extent. We have also attached our current brochure which should be used for the general content and information. PLEASE NOTE: Ignore the appraisals on the penultimate page - I will provide new ones in a separate document. (Use the one with 5 appraisals, not 3!)
The final design should be modern and attractive and should feature some images of the Middle East including some impressive buildings and new railways (similar to our current ones).
Please also link our website
and use it for inspiration: http://www.bk-worldwide.co.uk
Updates
We would like the brochure to be A5 and landscape - although it will only be emailed to clients and not printed.
There is no limit on number of pages.
There seems to be a problem opening the appraisals document I attached.
The content of this document is:
BK Worldwide Appraisals
"I had the pleasure of working with BK Worldwide as a client and found them to be a great recruiter with in-depth rail knowledge, I had great results from them time after time. I found the team very trustworthy, professional and fun to work with. I would highly recommend BK Worldwide and will continue to use the company for all my future recruitment needs"
Tarek Olivastro, Dunemark Transit Company
“When looking to advance my career, I enquired with BK Worldwide about a senior position in the Middle East. I dealt specifically with Colin who I found very helpful. He informed me of all the job requirements, the background of the role, responsibilities and package. Colin was extremely diligent in moving the process forward and throughout kept in contact and abreast of the situation. In all it proved a great success and I am now happily placed in my new role. Even though Colin performed beyond the normal boundaries of his role he even now keeps in contact to make sure everything is ok and all parties happy and satisfied with the outcome. I wholeheartedly endorse Colin and BK Worldwide and will use them when I am next supplementing my team.”
Miles Thornbury, Head of Quantity Surveying, Vellum Gulf Design Partners (VGDP), Kuwait
BK Worldwide is a recruitment company that has an insatiable appetite for understanding the jobs, for which they recruit, and not only the jobs, but they also establish excellent rapport with the clients and candidates. They are always there when I need to fill positions in my organization quickly. They listen to what I need and always supply me with the resumes that I could review right away to start hiring who I needed - saving me time and effort. They are always able to supply me with the exact person that I need for the open position."
Nadia Faris, HR Consultant, Dunemark Transit
Target Market(s)
Professional clients in the Middle East
Industry/Entity Type
Construction
Colors
Designer to choose colors to be used in the design.
Look and feel

```html
<!DOCTYPE html>
<html lang="en">
<head>
<meta charset="utf-8">
<title>Sectors We Recruit For</title>
<link rel="stylesheet" href="https://fonts.googleapis.com/css2?family=Questrial&display=swap">
<style>
  :root {
    --page: #ffffff;
    --panel: #e2e2e2;
    --panel-shadow: rgba(0, 0, 0, 0.35);
    --ink: #1e1e1e;
    --label: #3d6597;
    --label-ink: #ffffff;
    --teal: #17a388;
  }
  * { box-sizing: border-box; margin: 0; padding: 0; }
  html, body { width: 1200px; height: 777px; overflow: hidden; background: var(--page); }
  .sheet {
    position: relative;
    width: 1200px;
    height: 777px;
    overflow: hidden;
    background: var(--page);
    font-family: "Questrial", "Century Gothic", sans-serif;
  }
  .base-wave { position: absolute; left: 0; top: 0; width: 1200px; height: 777px; }
  .sector {
    position: absolute;
    top: 0;
    width: 281px;
    height: 777px;
    background: var(--panel);
    box-shadow: 3px 0 4px var(--panel-shadow);
  }
  .sector--architecture { left: 23px; }
  .sector--civil { left: 315px; }
  .sector--construction { left: 607px; }
  .sector--surveying { left: 900px; }
  .sector__photo { position: absolute; left: 0; top: 0; width: 281px; height: 310px; display: block; }
  .sector__services {
    position: absolute;
    left: 0;
    width: 281px;
    transform: translateY(-50%);
    text-align: center;
    font-size: 23px;
    line-height: 25.5px;
    color: var(--ink);
    white-space: nowrap;
  }
  .sector--architecture .sector__services { top: 469px; }
  .sector--civil .sector__services { top: 465px; }
  .sector--construction .sector__services { top: 464px; }
  .sector--surveying .sector__services { top: 447px; }
  .sector__label {
    position: absolute;
    left: 12px;
    top: 654px;
    width: 259px;
    height: 69px;
    background: var(--label);
    color: var(--label-ink);
    display: flex;
    align-items: center;
    justify-content: center;
    text-align: center;
    font-size: 23.5px;
    line-height: 28px;
    font-weight: 400;
    text-transform: uppercase;
    white-space: nowrap;
    box-shadow: 0 5px 5px -2px rgba(0, 0, 0, 0.3);
  }
  .sector--civil .sector__label { left: 13px; }
  .sector--construction .sector__label { left: 9px; }
  .sector--surveying .sector__label { left: 13px; }
</style>
</head>
<body>
<main class="sheet">
  <svg class="base-wave" viewBox="0 0 1200 777" aria-hidden="true">
    <path d="M0 777 L0 742 Q600 640 1200 742 L1200 777 Z" fill="var(--teal)"/>
  </svg>

  <section class="sector sector--architecture">
    <svg class="sector__photo" viewBox="0 0 281 310" role="img" aria-label="Photo of modern towers behind palm trees in a Gulf city">
      <defs>
        <linearGradient id="sky-arch" x1="0" y1="0" x2="0" y2="1">
          <stop offset="0" stop-color="#4a78c4"/>
          <stop offset="0.55" stop-color="#8fb0dc"/>
          <stop offset="1" stop-color="#3f6b3a"/>
        </linearGradient>
      </defs>
      <path d="M0 0 H281 V278 Q150 236 0 204 Z" fill="url(#sky-arch)"/>
    </svg>
    <p class="sector__services">New Builds,<br>Regeneration,<br>Conservation,<br>Landscape Architecture,<br>Urban Design,<br>Master planning,<br>Commercial and<br>Redevelopment</p>
    <h2 class="sector__label">Architecture</h2>
  </section>

  <section class="sector sector--civil">
    <svg class="sector__photo" viewBox="0 0 281 310" role="img" aria-label="Photo of a waterfront skyline with a speedboat on the sea">
      <defs>
        <linearGradient id="sky-civil" x1="0" y1="0" x2="0" y2="1">
          <stop offset="0" stop-color="#3f86d4"/>
          <stop offset="0.6" stop-color="#a9c8e6"/>
          <stop offset="0.78" stop-color="#2f6f9c"/>
          <stop offset="1" stop-color="#1c4f74"/>
        </linearGradient>
      </defs>
      <path d="M0 0 H281 V301 Q140 296 0 278 Z" fill="url(#sky-civil)"/>
    </svg>
    <p class="sector__services">Coastal and Marine,<br>Environmental,<br>Geotechnical, Structural,<br>Highways, Bridges, Rail,<br>Tunnelling, Airports/Ports,<br>Transport planning,<br>Power, Water,<br>Public Health,<br>Risk Management and<br>Project Management</p>
    <h2 class="sector__label">Civil &amp; Structural<br>Engineering</h2>
  </section>

  <section class="sector sector--construction">
    <svg class="sector__photo" viewBox="0 0 281 310" role="img" aria-label="Photo of a metro train on an elevated track between towers">
      <defs>
        <linearGradient id="sky-cons" x1="0" y1="0" x2="0" y2="1">
          <stop offset="0" stop-color="#7fa8d4"/>
          <stop offset="0.5" stop-color="#c9d8e6"/>
          <stop offset="0.7" stop-color="#8a97a4"/>
          <stop offset="1" stop-color="#4d5056"/>
        </linearGradient>
      </defs>
      <path d="M0 0 H281 V287 Q140 300 0 301 Z" fill="url(#sky-cons)"/>
    </svg>
    <p class="sector__services">Construction<br>Management,<br>Design &amp; Build,<br>Facilities Management<br>and Building Services</p>
    <h2 class="sector__label">Construction<br>&amp; Building Services</h2>
  </section>

  <section class="sector sector--surveying">
    <svg class="sector__photo" viewBox="0 0 281 310" role="img" aria-label="Photo of an illuminated city skyline at night">
      <defs>
        <linearGradient id="sky-surv" x1="0" y1="0" x2="0" y2="1">
          <stop offset="0" stop-color="#5d6f86"/>
          <stop offset="0.45" stop-color="#1e3a55"/>
          <stop offset="0.8" stop-color="#1f6a5a"/>
          <stop offset="1" stop-color="#2c9a58"/>
        </linearGradient>
      </defs>
      <path d="M0 0 H281 V204 Q140 255 0 278 Z" fill="url(#sky-surv)"/>
    </svg>
    <p class="sector__services">Building Surveying,<br>Land surveying,<br>Quantity Surveying,<br>Rural Practice and<br>Hydrographic Surveying</p>
    <h2 class="sector__label">Surveying</h2>
  </section>
</main>
</body>
</html>
```